General Contractors need a new Crisp updated Card Design

We need a new business card design for our company of 25 years based in Toronto call Holvaster Building Inc. : Our goal is to be the leading commercial contractors in Toronto by providing exceptional value to our clients. We work very hard to deliver professional, quality, service in conjunction with consistent price competitiveness to all of our clients on every single project.

Target Market(s)

Design & Build Clients

Industry/Entity Type

Construction Company

Contact Information for Business Card

Address:
18 North Tamlin Glen Road, Unit 57, Marbrook Vale, ON, K7T 2R9
Office: 905-218-5937

Holvasters Logo
Employee Job Description
Employee Cell Phone #
Employee Email
www.holvaster-example.com

Colors

Designer to choose colors to be used in the design.

Requirements
Must have
• Quote Company Saying:
• "Professional. Quality. Service."
Nice to have
• New Crisp up to date look. simple & fresh ( Not to Busy)
Should not have
• NO BLUE PRINTS ON THE BUSINESS CARDS

```html
<!DOCTYPE html>
<html lang="en">
<head>
<meta charset="utf-8">
<title>Holvaster Building Inc. – Business Card</title>
<link rel="stylesheet" href="https://fonts.googleapis.com/css2?family=Lato:wght@400;700&family=Libre+Baskerville:wght@700&display=swap">
<style>
  :root {
    --teal: #00706a;
    --teal-dark: #0b4e49;
    --mint: #b0c8bf;
    --white: #ffffff;
    --ink: #2f3432;
    --grey: #55605c;
    --stage: #1f2121;
    --serif: "Libre Baskerville", Georgia, serif;
    --sans: "Lato", Arial, sans-serif;
  }
  * { box-sizing: border-box; margin: 0; padding: 0; }
  html, body {
    width: 1200px; height: 960px; overflow: hidden;
    background: var(--stage);
  }
  .canvas { position: relative; width: 1200px; height: 960px; }

  .card {
    position: absolute;
    width: 560px; height: 320px;
    overflow: hidden;
    box-shadow: 0 14px 36px rgba(0,0,0,.45);
  }

  /* Back side */
  .card-back { left: 320px; top: 90px; background: var(--mint); }
  .back-brand {
    position: absolute; left: 0; right: 0; top: 104px;
    display: flex; align-items: center; justify-content: center; gap: 16px;
  }
  .back-brand .brand-square { width: 40px; height: 40px; background: var(--teal); }
  .back-brand .brand-name {
    font-family: var(--serif); font-weight: 700; font-size: 30px;
    letter-spacing: 2px; color: var(--teal); text-transform: uppercase;
  }
  .back-saying {
    position: absolute; left: 0; right: 0; top: 170px; text-align: center;
    font-family: var(--serif); font-weight: 700; font-size: 14px;
    letter-spacing: 2px; color: var(--teal-dark);
  }
  .back-url {
    position: absolute; left: 0; right: 0; top: 246px; text-align: center;
    font-family: var(--sans); font-size: 17px; letter-spacing: 3px; color: var(--teal);
  }

  /* Front side */
  .card-front { left: 320px; top: 530px; background: var(--white); }
  .front-shapes { position: absolute; inset: 0; }
  .front-brand {
    position: absolute; left: 26px; top: 26px;
    display: flex; align-items: center; gap: 12px;
  }
  .front-brand .brand-square { width: 44px; height: 44px; background: var(--teal); }
  .front-brand .brand-name {
    font-family: var(--serif); font-weight: 700; font-size: 19px; line-height: 1.15;
    letter-spacing: 1px; color: var(--teal); text-transform: uppercase;
  }
  .contact-list {
    position: absolute; left: 26px; top: 114px; list-style: none;
    font-family: var(--sans); font-size: 13px; line-height: 21px; color: var(--grey);
  }
  .contact-list li { display: flex; align-items: center; gap: 7px; }
  .contact-list svg { width: 11px; height: 11px; fill: var(--grey); flex: none; }
  .person {
    position: absolute; right: 28px; top: 34px; text-align: right;
  }
  .person-name {
    font-family: var(--serif); font-weight: 700; font-size: 16px;
    letter-spacing: 1px; color: var(--ink);
  }
  .person-title {
    font-family: var(--serif); font-weight: 700; font-size: 13px;
    letter-spacing: 1px; color: var(--teal); margin-top: 2px;
  }
  .address {
    position: absolute; right: 26px; top: 238px;
    display: flex; align-items: center; gap: 8px;
    font-family: var(--sans); font-style: normal; font-size: 13px; line-height: 19px;
    color: var(--white); text-align: right;
  }
  .address svg { width: 12px; height: 16px; fill: var(--white); flex: none; }
</style>
</head>
<body>
<main class="canvas">

  <section class="card card-back" aria-label="Business card, back">
    <div class="back-brand">
      <span class="brand-square"></span>
      <span class="brand-name">Holvaster Building</span>
    </div>
    <p class="back-saying">Professional. Quality. Service.</p>
    <p class="back-url">www.holvaster-example.com</p>
  </section>

  <section class="card card-front" aria-label="Business card, front">
    <svg class="front-shapes" viewBox="0 0 560 320" aria-hidden="true">
      <polygon fill="var(--mint)" points="0,100 392,100 346,126 300,126 258,172 150,224 0,224"/>
      <polygon fill="var(--teal)" points="280,118 560,228 560,320 350,320"/>
      <polygon fill="var(--teal-dark)" points="168,252 272,202 322,320 232,320"/>
    </svg>

    <div class="front-brand">
      <span class="brand-square"></span>
      <span class="brand-name">Holvaster<br>Building Inc.</span>
    </div>

    <ul class="contact-list">
      <li><svg viewBox="0 0 12 12"><path d="M2.5 1l2 2.3-1 1.2a7 7 0 0 0 4 4l1.2-1 2.3 2-1.3 1.5C5 11 1 7 1 2.3z"/></svg>905-218-5937</li>
      <li><svg viewBox="0 0 12 12"><path d="M3 0h6v12H3zm1 1.5v8h4v-8z"/></svg>905-604-1178</li>
      <li><svg viewBox="0 0 12 12"><path d="M0 2h12v8H0zm1 1v.4l5 3.4 5-3.4V3z"/></svg>info@holvaster-example.com</li>
      <li><svg viewBox="0 0 12 12"><path d="M6 0a6 6 0 1 0 0 12A6 6 0 0 0 6 0zm0 1.2c.8.8 1.3 2.5 1.4 4.2H4.6C4.7 3.7 5.2 2 6 1.2zM1.2 6.6h2.2c.1 1.6.5 3 1.1 4A4.8 4.8 0 0 1 1.2 6.6zm0-1.2a4.8 4.8 0 0 1 3.3-4c-.6 1-1 2.4-1.1 4zm4.8 5.4c-.8-.8-1.3-2.5-1.4-4.2h2.8c-.1 1.7-.6 3.4-1.4 4.2zm1.5-.2c.6-1 1-2.4 1.1-4h2.2a4.8 4.8 0 0 1-3.3 4zm1.1-5.2c-.1-1.6-.5-3-1.1-4a4.8 4.8 0 0 1 3.3 4z"/></svg>www.holvaster-example.com</li>
    </ul>

    <div class="person">
      <p class="person-name">DANA CORLISS</p>
      <p class="person-title">PRESIDENT</p>
    </div>

    <address class="address">
      <span>18 North Tamlin Glen Road<br>Unit 57, Marbrook Vale<br>ON, K7T 2R9</span>
      <svg viewBox="0 0 12 16"><path d="M6 0a6 6 0 0 0-6 6c0 4.5 6 10 6 10s6-5.5 6-10a6 6 0 0 0-6-6zm0 8.5A2.5 2.5 0 1 1 6 3.5a2.5 2.5 0 0 1 0 5z"/></svg>
    </address>
  </section>

</main>
</body>
</html>
```